Brindle Works ~ Business Card Design Project

Brindle Works is a digital marketing agency which creates and maintains online social presence for brands and businesses. Services include monthly stream management, social media advertising campaigns, online press release distribution, search engine optimization, copywriting, digital strategy consultation, video marketing campaigns, fan acquisition, and Wordpress website development.
The company is currently rebranding to a full service agency from just a social media firm, with a new website launching soon. I'm looking for an extremely creative and modern business card design that pops out from the rest and fits with our company's sector/services.
It will need to be 1039 x 697 pixels, and rectangular (not rounded edges or corners). Utilize our company logo (file is attached), and include the following information in any design or layout:
Martin Okafor
CEO/Creative Director
Brindle Works
Gatherly: facebook.com/brindleworks
Twitter: @BrindleWorks
Phone: +1 555 014 8892
Cell: +1 555 017 4410
Email: martin@brindleworks.example
Website: www.brindleworks.example
418 Pellham Crescent, Suite 302
Ashbury, ON
K7Q 3V8

```html
<!DOCTYPE html>
<html lang="en">
<head>
<meta charset="utf-8">
<title>Brindle Works — Business Card</title>
<link href="https://fonts.googleapis.com/css2?family=Ubuntu:wght@400;500;700&display=swap" rel="stylesheet">
<style>
  :root {
    --stage: #e6e6e6;
    --sheet: #ffffff;
    --label: #a9a9a9;
    --card-red: #d51f27;
    --card-red-deep: #c21b22;
    --card-white: #ffffff;
    --navy: #2b3990;
    --blue: #1b75bb;
    --ink-light: #ffffff;
    --icon-tile: #f2d5d6;
  }
  * { margin: 0; padding: 0; box-sizing: border-box; }
  html, body { width: 1200px; height: 900px; overflow: hidden; }
  body {
    background: var(--stage);
    font-family: "Ubuntu", Arial, sans-serif;
    position: relative;
  }
  .sheet {
    position: absolute;
    left: 70px; top: 60px;
    width: 1060px; height: 780px;
    background: var(--sheet);
  }
  .side-label {
    position: absolute;
    font-size: 27px;
    color: var(--label);
    font-weight: 400;
  }
  .side-label--front { left: 170px; top: 100px; }
  .side-label--back { left: 917px; top: 435px; }

  .card {
    position: absolute;
    width: 510px; height: 342px;
    overflow: hidden;
    box-shadow: 0 4px 14px rgba(0,0,0,0.22);
  }
  .card__shape { position: absolute; inset: 0; width: 100%; height: 100%; }

  /* Front */
  .card--front { left: 150px; top: 145px; background: var(--card-white); }
  .front-brand {
    position: absolute;
    left: 62px; top: 100px;
    display: flex; align-items: center; gap: 20px;
  }
  .front-brand__mark {
    width: 96px; height: 96px; border-radius: 50%;
    background: var(--navy);
    flex: none;
  }
  .front-brand__name {
    font-size: 44px; font-weight: 500;
    color: var(--navy);
    letter-spacing: -0.5px;
    white-space: nowrap;
  }
  .front-person {
    position: absolute;
    left: 228px; top: 218px;
    line-height: 1.3;
  }
  .front-person__name {
    font-size: 17px; font-weight: 700; color: var(--navy);
    text-transform: uppercase; letter-spacing: 0.2px;
  }
  .front-person__role,
  .front-person__company { font-size: 16px; color: var(--blue); }

  /* Back */
  .card--back { left: 465px; top: 470px; background: var(--card-red); color: var(--ink-light); }
  .back-faint-mark {
    position: absolute;
    left: 30px; top: 120px;
    width: 150px; height: 150px; border-radius: 50%;
    background: var(--card-red-deep);
  }
  .social-list { position: absolute; left: 46px; top: 38px; list-style: none; }
  .social-list__item {
    display: flex; align-items: center; gap: 8px;
    font-size: 16.5px; margin-bottom: 14px;
    white-space: nowrap;
  }
  .social-list__tile {
    width: 30px; height: 30px; border-radius: 3px;
    background: var(--icon-tile);
    flex: none;
  }
  .contact {
    position: absolute;
    right: 40px; top: 170px;
    text-align: right;
    font-size: 16px; line-height: 1.3;
    font-style: normal;
    white-space: nowrap;
  }
  .contact strong { font-weight: 700; }
  .contact__address { margin-top: 16px; }
</style>
</head>
<body>
  <div class="sheet"></div>

  <span class="side-label side-label--front">Front</span>
  <span class="side-label side-label--back">Back</span>

  <section class="card card--front" aria-label="Business card front">
    <svg class="card__shape" viewBox="0 0 510 342" preserveAspectRatio="none" aria-hidden="true">
      <path d="M0 0 H178 C80 22 18 100 10 210 L0 210 Z" fill="var(--card-red)"/>
    </svg>
    <div class="front-brand">
      <span class="front-brand__mark"></span>
      <span class="front-brand__name">Brindle Works</span>
    </div>
    <div class="front-person">
      <p class="front-person__name">Martin Okafor</p>
      <p class="front-person__role">CEO/Creative Director</p>
      <p class="front-person__company">Brindle Works</p>
    </div>
  </section>

  <section class="card card--back" aria-label="Business card back">
    <svg class="card__shape" viewBox="0 0 510 342" preserveAspectRatio="none" aria-hidden="true">
      <path d="M330 0 H510 V190 C505 80 440 5 330 0 Z" fill="var(--card-white)"/>
    </svg>
    <span class="back-faint-mark"></span>
    <ul class="social-list">
      <li class="social-list__item"><span class="social-list__tile"></span>gatherly.example/brindleworks</li>
      <li class="social-list__item"><span class="social-list__tile"></span>@BrindleWorks</li>
    </ul>
    <address class="contact">
      <p>P: <strong>1 555 014 8892</strong></p>
      <p>C: <strong>1 555 017 4410</strong></p>
      <p>E: martin@brindleworks.example</p>
      <p>W: www.brindleworks.example</p>
      <p class="contact__address">418 Pellham Crescent, Suite 302</p>
      <p>Ashbury, ON. K7Q 3V8</p>
    </address>
  </section>
</body>
</html>
```